Lead Generation Landing Page Design For Marketing Agency's New White Label Product

We are a marketing agency that just launched out white label platform.

We need to create a nice landing page that gets people excited.

I have attached a pdf of the content and instructions.

Please note that I have also uploaded images that go with the highlighted yellow content in the instructions pdf.

Please be sure to use the images to compliment the content for the highlighted yellow parts of the pdf and use the images that are consistent with the name of the content.

For for the rest of the content you can simply use bullets of some sort.

Please be sure to keep the theme same at www.brightlanternpromoworks.biz as this is where the page will be hosted.

Be sure to show me mock ups with my header and footer from my current site www.brightlanternpromoworks.biz

Target Market(s)

Marketing Agencies, Media Buyers, Entrepreneurs, Millionaires

Industry/Entity Type

Cash Flow

Requirements
Must have
• must use current header and footer from current website www.brightlanternpromoworks.biz as this is where the page will be hosted
Nice to have
Should not have
• na

```html
<!DOCTYPE html>
<html lang="en">
<head>
<meta charset="utf-8">
<title>White Label Partner Program – Bright Lantern Promo Works</title>
<link href="https://fonts.googleapis.com/css2?family=Montserrat:wght@500;600;700;800&family=Poppins:wght@400;500;600&display=swap" rel="stylesheet">
<style>
:root{
  --navy:#1c1f5c;
  --navy-deep:#0c0e33;
  --violet:#3a1f8a;
  --blue:#2747c9;
  --ink:#1d1f33;
  --muted:#5b5f73;
  --green:#3fd43a;
  --green-dark:#22a81e;
  --white:#ffffff;
  --soft:#f4f5fb;
  --footer:#1f2336;
  --footer-line:#2f3450;
  --red:#e2262b;
}
*{box-sizing:border-box;margin:0;padding:0}
html,body{width:1200px;height:4884px;overflow:hidden}
body{font-family:"Poppins",Arial,sans-serif;color:var(--ink);background:var(--white)}
h1,h2,h3{font-family:"Montserrat",Arial,sans-serif}

/* header */
.topbar{height:52px;display:flex;align-items:center;justify-content:space-between;padding:0 40px;background:var(--white)}
.brand{display:flex;align-items:center;gap:10px;font-family:"Montserrat",Arial,sans-serif;font-weight:800;font-size:20px;color:var(--blue);letter-spacing:.5px}
.brand-dot{width:22px;height:22px;border-radius:50%;background:var(--blue)}
.account{display:flex;gap:24px;font-size:14px;color:var(--ink)}
.account span{display:flex;align-items:center;gap:6px}
.account i{width:18px;height:18px;border-radius:50%;background:var(--blue);display:inline-block}
.mainnav{height:44px;background:var(--navy);display:flex;align-items:center;justify-content:space-between;padding:0 40px}
.mainnav ul{display:flex;gap:30px;list-style:none;color:var(--white);font-size:13px;font-weight:500}
.nav-cta{display:flex;gap:12px}
.btn{display:inline-block;background:var(--green);color:var(--ink);font-family:"Montserrat",Arial,sans-serif;font-weight:700;border-radius:3px;text-align:center}
.nav-cta .btn{font-size:12px;padding:7px 16px}

/* hero */
.hero{height:544px;position:relative;text-align:center;color:var(--white);overflow:hidden}
.hero-art{position:absolute;inset:0;background:radial-gradient(ellipse at 50% 85%,#5a3bd1 0%,#2b1a7a 35%,#120f45 70%,var(--navy-deep) 100%)}
.hero-copy{position:relative;padding-top:144px}
.hero h1{font-size:34px;font-weight:700;line-height:1.35;width:820px;margin:0 auto}
.hero p{margin-top:28px;font-size:17px;opacity:.9}

/* intro */
.intro{height:300px;text-align:center;padding-top:108px}
.intro h2{font-size:38px;font-weight:800;color:var(--blue);line-height:1.2}
.intro h3{font-size:30px;font-weight:500;color:var(--ink);margin-top:4px}

/* features */
.features{height:2140px}
.feature{height:356px;display:flex;align-items:center;justify-content:center;gap:56px}
.feature.flip{flex-direction:row-reverse}
.screen{width:400px;height:250px;border-radius:10px 10px 4px 4px;background:linear-gradient(160deg,#2c2f3f,#111320);padding:12px;position:relative}
.screen::after{content:"";position:absolute;left:-30px;right:-30px;bottom:-12px;height:12px;background:#c9ccd6;border-radius:0 0 10px 10px}
.screen-fill{width:100%;height:100%;border-radius:2px}
.fill-a{background:linear-gradient(180deg,#e9ecf4,#bfc6da)}
.fill-b{background:linear-gradient(135deg,#9b2f86,#4d2c8e)}
.fill-c{background:linear-gradient(135deg,#203048,#51617a)}
.fill-d{background:linear-gradient(180deg,#f7f8fb,#dde2ee)}
.fill-e{background:linear-gradient(180deg,#eef0f6,#c7cedf)}
.fill-f{background:linear-gradient(180deg,#f3f5fa,#d6dbe8)}
.feature-text{width:380px}
.feature-text h3{font-size:24px;font-weight:700;color:var(--blue);line-height:1.25}
.feature-text p{margin-top:12px;font-size:14px;line-height:1.55;color:var(--muted)}
.access{text-align:center;padding-top:6px}
.access .btn{font-size:14px;padding:14px 30px}

/* sub user features */
.perks{height:720px;position:relative;color:var(--white);background:linear-gradient(180deg,#1b1650,#110e3a)}
.globe{position:absolute;left:60px;top:140px;width:520px;height:460px;border-radius:50%;background:radial-gradient(circle at 45% 45%,#5b46d9 0%,#2d2384 45%,rgba(27,22,80,0) 72%)}
.perks-body{position:absolute;left:640px;top:88px;width:500px}
.perks h2{font-size:30px;font-weight:700;line-height:1.3}
.perks ul{list-style:none;margin-top:26px}
.perks li{display:flex;gap:12px;font-size:13.5px;line-height:1.45;margin-bottom:11px}
.perks li svg{flex:none;margin-top:1px}

/* disclaimer */
.disclaimer{height:340px;text-align:center;padding-top:100px}
.disclaimer p{width:860px;margin:0 auto;font-size:19px;line-height:1.6;color:var(--ink)}
.disclaimer strong{font-family:"Montserrat",Arial,sans-serif;font-weight:800}
.disclaimer .btn{margin-top:40px;font-size:15px;padding:14px 74px}

/* footer */
.site-footer{height:600px;background:var(--footer);color:#c9cce0;display:flex;padding:72px 60px 0;gap:70px}
.foot-brand{width:300px}
.foot-brand .brand{color:var(--white)}
.socials{display:flex;gap:10px;margin-top:28px}
.socials span{width:34px;height:34px;border-radius:50%;background:#3b4160}
.foot-brand .btn{margin-top:24px;font-size:12px;padding:10px 20px}
.foot-col h4{font-family:"Montserrat",Arial,sans-serif;color:var(--white);font-size:14px;font-weight:700;margin-bottom:18px;letter-spacing:.5px}
.foot-col p,.foot-col li{font-size:12px;line-height:1.7}
.foot-col p+p{margin-top:12px}
.foot-col ul{list-style:none}
.contact{width:270px}
.links{width:190px}
.legal{height:44px;background:#161a2b;display:flex;align-items:center;justify-content:space-between;padding:0 60px;font-size:11px;color:#9ea2bc}
.legal-mark{width:22px;height:22px;background:var(--red);border-radius:3px}
</style>
</head>
<body>

<header>
  <div class="topbar">
    <div class="brand"><span class="brand-dot"></span>BRIGHT LANTERN PROMO WORKS</div>
    <div class="account"><span><i></i>Login</span><span><i></i>Sign Up</span></div>
  </div>
  <nav class="mainnav">
    <ul>
      <li>Home</li><li>Incentives List</li><li>White Label</li><li>Risk Free Trial</li><li>Integrations</li><li>Industries ▾</li>
    </ul>
    <div class="nav-cta"><span class="btn">Call or Text ▾</span><span class="btn">Book a Call ▾</span></div>
  </nav>
</header>

<section class="hero">
  <div class="hero-art" role="img" aria-label="Glowing purple particle field stretching toward the horizon"></div>
  <div class="hero-copy">
    <h1>Resell Unlimited Sub User Accounts For Any Price You Wish &amp; Keep 100% of The Revenue.</h1>
    <p>Your Very Own BLP Platform Under Your Own Website &amp; Brand...</p>
  </div>
</section>

<section class="intro">
  <h2>All of this IS YOURS as an Authorized</h2>
  <h3>BLP White Label Partner</h3>
</section>

<section class="features">
  <article class="feature">
    <div class="screen"><div class="screen-fill fill-a" role="img" aria-label="Laptop screen showing API sign up form"></div></div>
    <div class="feature-text"><h3>Simple API Integration</h3><p>Sign Up New Sub Users From Your Own URL Using Our API Integration</p></div>
  </article>
  <article class="feature flip">
    <div class="screen"><div class="screen-fill fill-b" role="img" aria-label="Laptop screen showing branded login page"></div></div>
    <div class="feature-text"><h3>True White Label Login Page</h3><p>Your Users Sign In To Their Account On Your Own URL Branded With Your Logo</p></div>
  </article>
  <article class="feature">
    <div class="screen"><div class="screen-fill fill-c" role="img" aria-label="Laptop screen showing the online redemption website"></div></div>
    <div class="feature-text"><h3>Totally Separate Redemption Website Than BLP's Redemption Website</h3><p>We Do This To Ensure No Trace Back To BLP</p></div>
  </article>
  <article class="feature flip">
    <div class="screen"><div class="screen-fill fill-d" role="img" aria-label="Laptop screen showing sub user management table"></div></div>
    <div class="feature-text"><h3>Your Own Sub User Management Database System</h3><p>Manage All Your Users From One Central Location</p></div>
  </article>
  <article class="feature">
    <div class="screen"><div class="screen-fill fill-e" role="img" aria-label="Laptop screen showing content upload panel"></div></div>
    <div class="feature-text"><h3>Ability To Upload Your Own Content For Your Sub Users To Access</h3><p>Upload Content That Adds Additional Value For Your Customers</p></div>
  </article>
  <article class="feature flip">
    <div class="screen"><div class="screen-fill fill-f" role="img" aria-label="Laptop screen showing custom plan builder"></div></div>
    <div class="feature-text"><h3>Create Unlimited Custom Plans</h3><p>Create Custom Plans Based On What Certificates To Include In Each Plan</p></div>
  </article>
  <div class="access"><span class="btn">GET ACCESS BUTTON</span></div>
</section>

<section class="perks">
  <div class="globe" role="img" aria-label="Glowing digital globe made of connected points"></div>
  <div class="perks-body">
    <h2>Your Sub Users Get Access To All These Features</h2>
    <ul>
      <li><svg width="16" height="16" viewBox="0 0 16 16"><circle cx="8" cy="8" r="8" fill="#3fd43a"/><path d="M4.5 8.2l2.3 2.3 4.7-4.8" stroke="#fff" stroke-width="1.8" fill="none"/></svg>Unlimited Access To All Our Incentives In 6 Categories (2, 3, 4-Night and Vegas hotel stay</li>
      <li><svg width="16" height="16" viewBox="0 0 16 16"><circle cx="8" cy="8" r="8" fill="#3fd43a"/><path d="M4.5 8.2l2.3 2.3 4.7-4.8" stroke="#fff" stroke-width="1.8" fill="none"/></svg>Certificates are not included with white label platform)</li>
      <li><svg width="16" height="16" viewBox="0 0 16 16"><circle cx="8" cy="8" r="8" fill="#3fd43a"/><path d="M4.5 8.2l2.3 2.3 4.7-4.8" stroke="#fff" stroke-width="1.8" fill="none"/></svg>Unlimited E-Certificates</li>
      <li><svg width="16" height="16" viewBox="0 0 16 16"><circle cx="8" cy="8" r="8" fill="#3fd43a"/><path d="M4.5 8.2l2.3 2.3 4.7-4.8" stroke="#fff" stroke-width="1.8" fill="none"/></svg>Unlimited SMS Certificates</li>
      <li><svg width="16" height="16" viewBox="0 0 16 16"><circle cx="8" cy="8" r="8" fill="#3fd43a"/><path d="M4.5 8.2l2.3 2.3 4.7-4.8" stroke="#fff" stroke-width="1.8" fill="none"/></svg>Unlimited Web Banner Certificates</li>
      <li><svg width="16" height="16" viewBox="0 0 16 16"><circle cx="8" cy="8" r="8" fill="#3fd43a"/><path d="M4.5 8.2l2.3 2.3 4.7-4.8" stroke="#fff" stroke-width="1.8" fill="none"/></svg>Unlimited White Label Certificate Landing Pages</li>
      <li><svg width="16" height="16" viewBox="0 0 16 16"><circle cx="8" cy="8" r="8" fill="#3fd43a"/><path d="M4.5 8.2l2.3 2.3 4.7-4.8" stroke="#fff" stroke-width="1.8" fill="none"/></svg>Unlimited White Label Redemption Pages</li>
      <li><svg width="16" height="16" viewBox="0 0 16 16"><circle cx="8" cy="8" r="8" fill="#3fd43a"/><path d="M4.5 8.2l2.3 2.3 4.7-4.8" stroke="#fff" stroke-width="1.8" fill="none"/></svg>Unlimited Website Sticky Bar Certificates</li>
      <li><svg width="16" height="16" viewBox="0 0 16 16"><circle cx="8" cy="8" r="8" fill="#3fd43a"/><path d="M4.5 8.2l2.3 2.3 4.7-4.8" stroke="#fff" stroke-width="1.8" fill="none"/></svg>Unlimited Website Pop Up Certificates</li>
      <li><svg width="16" height="16" viewBox="0 0 16 16"><circle cx="8" cy="8" r="8" fill="#3fd43a"/><path d="M4.5 8.2l2.3 2.3 4.7-4.8" stroke="#fff" stroke-width="1.8" fill="none"/></svg>Unlimited QR Code Certificates</li>
      <li><svg width="16" height="16" viewBox="0 0 16 16"><circle cx="8" cy="8" r="8" fill="#3fd43a"/><path d="M4.5 8.2l2.3 2.3 4.7-4.8" stroke="#fff" stroke-width="1.8" fill="none"/></svg>Unlimited API E-Certificates</li>
      <li><svg width="16" height="16" viewBox="0 0 16 16"><circle cx="8" cy="8" r="8" fill="#3fd43a"/><path d="M4.5 8.2l2.3 2.3 4.7-4.8" stroke="#fff" stroke-width="1.8" fill="none"/></svg>Unlimited Automation E-Certificates</li>
      <li><svg width="16" height="16" viewBox="0 0 16 16"><circle cx="8" cy="8" r="8" fill="#3fd43a"/><path d="M4.5 8.2l2.3 2.3 4.7-4.8" stroke="#fff" stroke-width="1.8" fill="none"/></svg>Unlimited Premium Certificates</li>
      <li><svg width="16" height="16" viewBox="0 0 16 16"><circle cx="8" cy="8" r="8" fill="#3fd43a"/><path d="M4.5 8.2l2.3 2.3 4.7-4.8" stroke="#fff" stroke-width="1.8" fill="none"/></svg>Promo Videos, Posters &amp; Flyers To Help Them Promote The Incentives To Their Audience</li>
    </ul>
  </div>
</section>

<section class="disclaimer">
  <p><strong>Disclaimer:</strong> This is a True White Label platform where you are responsible for creating your own sales pages, etc. We simply provide you with the Sign Up API and the Sub User Management Tool to add users with.</p>
  <span class="btn">SIGN UP</span>
</section>

<footer class="site-footer">
  <div class="foot-brand">
    <div class="brand"><span class="brand-dot"></span>BRIGHT LANTERN PROMO WORKS</div>
    <div class="socials"><span></span><span></span><span></span><span></span><span></span></div>
    <span class="btn">Book A Call With Today</span>
  </div>
  <div class="foot-col contact">
    <h4>CONTACT US</h4>
    <p>Bright Lantern Promo Works, Inc.<br>1200 Harbor Light Ave, Suite 40<br>Portland, OR 97201</p>
    <p>Call Or Text Us<br>Main Office: (555) 014-2288<br>Customer Support: (555) 014-2290</p>
    <p>Web, Email &amp; Online Support<br>support@brightlanternpromoworks.biz<br>Available Mon–Fri, 9am–6pm PT</p>
  </div>
  <div class="foot-col links">
    <h4>QUICK LINKS</h4>
    <ul><li>Home</li><li>Incentives List</li><li>Login</li><li>Sign Up</li><li>Affiliates</li><li>Integrations</li><li>Testimonials</li><li>Industries</li><li>White Label Platform</li><li>Risk Free Trial</li><li>Reseller Program</li><li>Support Center</li></ul>
  </div>
  <div class="foot-col links">
    <h4>OTHER LINKS</h4>
    <ul><li>Careers</li><li>Terms Of Service</li><li>Privacy Policy</li><li>Payment Options</li><li>Refund Policy</li><li>Incentive Redemption Help</li><li>Partner Resources</li></ul>
  </div>
</footer>
<div class="legal">
  <span>© 2024 Bright Lantern Promo Works, Inc. All Rights Reserved | www.brightlanternpromoworks.biz</span>
  <span class="legal-mark"></span>
</div>

</body>
</html>
```